Band Autograph Postcard

We are Silver Hollow a classically influenced - Gothic alternative - Progressive Rock band looking to have a postcard designed for us to mail out for autographs.

We would like to design this with our photos and have a layout that we can all sign underneath our pictures. Please create a design using the photos attached and we need this to be one cohesive design. We would also like to include our logo.

You can cut out the photos to fit your design needs.

Please incorporate the following into this design:

1. Band name (Silver Hollow) Ringbearer Font on the front
2. website: www.SilverHollowSounds.example on the front
3. Photos & Logo
4. Our links on the back of the postcard
www.Friendspace.example/SilverHollowSounds
www.tunehaven.example/SilverHollow
Follow us on chirpnet @SilverHollowSounds

5. A space to add mailing address
6. Dark colored tones

This postcard needs to be laid out for an oversized postcard we will be using printmorrow.example for our printing so please check the sizes.  We will be signing them so they will need to be able to read our signatures and not have the card be too black or too dark.

I uploaded a photo to show the layout.

```html
<!DOCTYPE html>
<html lang="en">
<head>
<meta charset="utf-8">
<title>Silver Hollow – Autograph Postcard</title>
<link href="https://fonts.googleapis.com/css2?family=Cinzel:wght@400;600&family=Cormorant+Garamond:ital,wght@1,500&display=swap" rel="stylesheet">
<style>
  :root {
    --backdrop: #d9d6d0;
    --card-black: #0b0b0b;
    --gold: #c9b27a;
    --gold-soft: #a8925c;
    --cream: #e9dfc3;
    --sign-white: #ffffff;
    --photo-light: #8a8a8a;
    --photo-dark: #1e1e1e;
  }
  * { box-sizing: border-box; margin: 0; padding: 0; }
  html, body {
    width: 1200px;
    height: 873px;
    overflow: hidden;
    background: var(--backdrop);
  }
  .postcard {
    position: absolute;
    left: 80px;
    top: 126px;
    width: 1040px;
    height: 620px;
    background: var(--card-black);
    box-shadow: 0 6px 24px rgba(0,0,0,0.25);
  }
  .brand-mark {
    position: absolute;
    left: 38px;
    top: 34px;
    display: flex;
    flex-direction: column;
    align-items: center;
    gap: 8px;
  }
  .brand-mark__dot {
    width: 30px;
    height: 30px;
    border-radius: 50%;
    background: var(--gold-soft);
  }
  .brand-mark__name {
    font-family: "Cinzel", serif;
    font-size: 13px;
    color: var(--cream);
    letter-spacing: 1px;
  }
  .masthead {
    position: absolute;
    left: 180px;
    right: 40px;
    top: 30px;
    text-align: center;
  }
  .masthead__title {
    font-family: "Cinzel", serif;
    font-weight: 400;
    font-size: 74px;
    letter-spacing: 6px;
    color: var(--cream);
    line-height: 1;
  }
  .masthead__site {
    margin-top: 14px;
    font-family: "Cormorant Garamond", serif;
    font-style: italic;
    font-weight: 500;
    font-size: 24px;
    letter-spacing: 3px;
    color: var(--cream);
  }
  .lineup {
    position: absolute;
    left: 60px;
    right: 60px;
    top: 200px;
    display: flex;
    justify-content: space-between;
  }
  .lineup__frame {
    width: 168px;
    height: 200px;
    border: 2px solid var(--gold);
    padding: 6px;
    background: #111;
  }
  .lineup__photo {
    width: 100%;
    height: 100%;
    background: radial-gradient(ellipse at 50% 40%, var(--photo-light) 0%, #4a4a4a 45%, var(--photo-dark) 100%);
  }
  .signing-band {
    position: absolute;
    left: 14px;
    right: 14px;
    bottom: 14px;
    height: 160px;
    background: var(--sign-white);
    outline: 2px solid var(--gold);
    outline-offset: 3px;
  }
</style>
</head>
<body>
  <section class="postcard">
    <div class="brand-mark">
      <span class="brand-mark__dot"></span>
      <span class="brand-mark__name">Silver Hollow</span>
    </div>

    <header class="masthead">
      <h1 class="masthead__title">Silver Hollow</h1>
      <p class="masthead__site">www.SilverHollowSounds.example</p>
    </header>

    <div class="lineup">
      <div class="lineup__frame"><div class="lineup__photo" role="img" aria-label="Black and white portrait of band member one"></div></div>
      <div class="lineup__frame"><div class="lineup__photo" role="img" aria-label="Black and white portrait of band member two"></div></div>
      <div class="lineup__frame"><div class="lineup__photo" role="img" aria-label="Black and white portrait of band member three"></div></div>
      <div class="lineup__frame"><div class="lineup__photo" role="img" aria-label="Black and white portrait of band member four with violin"></div></div>
      <div class="lineup__frame"><div class="lineup__photo" role="img" aria-label="Black and white portrait of band member five"></div></div>
    </div>

    <div class="signing-band" aria-label="Space for band autographs"></div>
  </section>
</body>
</html>
```